Planting the Lanternfield Harvest Garden:
A Household Compass for Growing Bright, Curious, and Kindly Patient Boys in Music and Work.
📘 Book Cover Design Brief – “Planting the Lanternfield Harvest Garden”

Project Title:
Design a bold, inspiring book cover for a best-selling book titled:
Planting the Lanternfield Harvest Garden
Subtitle: A Household Compass for Growing Bright, Curious, and Kindly Patient Boys in Music and Work

🎯 Audience:

Parents of female athletes ages 14–20 who want their daughters to build confidence, strength, resilience, and long-term success both in sports and in life.

This book should feel encouraging, empowering, and credible — NOT cheesy, childish, or overly academic.

📕 Design Tone & Style:

Powerful and professional — should feel like a best-selling book from a leading performance or parenting expert

Emotionally compelling — conveys hope, resilience, strength, and possibility

Visually modern and clean — avoid anything overly busy, cliché, or childish

Heroic/aspirational tone — think transformation, leadership, strong positioning

💡 Visual Direction / Ideas (Use as Inspiration, Not Limitation):

Strong, confident teenage female athlete imagery — adaptable beyond one specific sport

Symbolic visuals — e.g. athlete standing strong, on a starting line, looking bold into the future, silhouette, or power stance

Bold typography that feels clean and modern (e.g., Proxima Nova, Montserrat, Gotham, Bebas Neue, etc.)

A title that stands out clearly when viewed as a thumbnail on Quellora

Color tones: Empowering, modern, and strong: think deep blues, greens, purples, or golds — avoid playful pastels or overly girly themes

Potential imagery: textured backgrounds, motion, bravery, development, strength, growth, sport/action overlays

🔥 What the Cover MUST Communicate:

✅ This is for parents who want strong, confident female athletes
✅ It’s a guidebook for personal development AND sports performance
✅ It’s about creating “LANTERNFIELD” confidence — physically, mentally and emotionally
✅ The message is: You can help your daughter become her strongest, most confident self

📚 Back-of-Book Summary (for context):

"Planting the Lanternfield Harvest Garden" is a parent's blueprint to building girls who are strong in body, confident in mind, and ready to lead on and off the field. Through simple strategies around strength training, mindset, nutrition, and character development, this book gives parents the tools to help their daughters stay injury-resistant, break through mental barriers, and unlock their full potential — in sports and in life.

✅ Deliverables:

Full cover design (front, back, spine) for paperback
High-resolution files (print-ready)
Source files (PSD, AI, etc.)
3D mockup versions of the book (standing, flat, stack)

Target Market(s)

Industry/Entity Type

Fitness

Font styles to use
Sans Serif

Colors
FFF300
FFF600
FEFA6F
FFFEC7
FFFEE8

Requirements
Must have
• Bold Font
Should not have
• I don't want an image of a female athlete. I want this to be font based.

```html
<!DOCTYPE html>
<html lang="en">
<head>
<meta charset="utf-8">
<title>Planting the Lanternfield Harvest Garden — Cover</title>
<link rel="stylesheet" href="https://fonts.googleapis.com/css2?family=Bebas+Neue&family=Oswald:wght@500;600&display=swap">
<style>
  :root {
    --backdrop: #ececec;
    --cover-black: #0b0b0b;
    --cover-black-soft: #1a1a1a;
    --title-white: #ffffff;
    --gold-deep: #a88d45;
    --gold-mid: #c9b26a;
    --gold-light: #efe5a8;
    --subtitle-gold: #c8b06a;
  }
  * { margin: 0; padding: 0; box-sizing: border-box; }
  html, body {
    width: 1197px; height: 1200px; overflow: hidden;
    background: var(--backdrop);
  }
  .cover {
    position: absolute;
    left: 243px; top: 66px;
    width: 710px; height: 1064px;
    background:
      radial-gradient(ellipse at 30% 10%, var(--cover-black-soft) 0%, transparent 55%),
      radial-gradient(ellipse at 80% 70%, #151515 0%, transparent 60%),
      var(--cover-black);
    overflow: hidden;
  }
  .subtitle {
    position: absolute;
    left: 0; right: 0; top: 46px;
    text-align: center;
    font-family: "Oswald", sans-serif;
    font-weight: 500;
    font-size: 23px;
    line-height: 30px;
    letter-spacing: 0.5px;
    color: var(--subtitle-gold);
    text-transform: uppercase;
  }
  .figure-area {
    position: absolute;
    left: 200px; top: 540px;
    width: 370px; height: 410px;
    background: radial-gradient(ellipse at 50% 50%, rgba(222,204,140,0.45) 0%, rgba(190,165,95,0.18) 45%, transparent 72%);
  }
  .title {
    position: absolute;
    left: 0; top: 0;
    width: 710px; height: 800px;
  }
  .title text {
    font-family: "Bebas Neue", sans-serif;
  }
  .title .line-white { fill: var(--title-white); }
  .title .line-gold { fill: url(#goldSheen); }
  .brand {
    position: absolute;
    left: 0; right: 0; top: 886px;
    display: flex; flex-direction: column; align-items: center;
  }
  .brand-circle {
    width: 84px; height: 84px;
    border: 3px solid var(--gold-mid);
    border-radius: 50%;
  }
  .brand-name {
    margin-top: 20px;
    font-family: "Oswald", sans-serif;
    font-weight: 600;
    font-size: 24px;
    letter-spacing: 3px;
    color: var(--title-white);
  }
</style>
</head>
<body>
  <main class="cover">
    <p class="subtitle">A Household Compass for Growing Bright, Curious,<br>and Kindly Patient Boys in Music and Work</p>

    <div class="figure-area" role="img" aria-label="Gold silhouette of a leaping athlete"></div>

    <svg class="title" viewBox="0 0 710 800" aria-label="Planting the Lanternfield Harvest Garden">
      <defs>
        <linearGradient id="goldSheen" x1="0" y1="0" x2="1" y2="0">
          <stop offset="0" stop-color="#a88d45"/>
          <stop offset="0.5" stop-color="#efe5a8"/>
          <stop offset="1" stop-color="#a88d45"/>
        </linearGradient>
      </defs>
      <text class="line-white" x="56" y="236" font-size="172" textLength="610" lengthAdjust="spacingAndGlyphs">PLANTING THE</text>
      <text class="line-gold" x="56" y="357" font-size="149" textLength="610" lengthAdjust="spacingAndGlyphs">LANTERNFIELD</text>
      <text class="line-white" x="56" y="569" font-size="280" textLength="610" lengthAdjust="spacingAndGlyphs">HARVEST</text>
      <text class="line-white" x="56" y="761" font-size="257" textLength="610" lengthAdjust="spacingAndGlyphs">GARDEN</text>
    </svg>

    <div class="brand">
      <div class="brand-circle"></div>
      <div class="brand-name">LANTERNFIELD</div>
    </div>
  </main>
</body>
</html>
```